Prepared ready to cook meal delivery service needs a flyer design

We need a flyer design for a startup company based in Cape Town, South Africa. I've attached a few flyer designs that I like.

The company is called 'Pemblo' and our website will be found at pemblo.co.za. We don't have a logo yet.

Flyer text:

Pemblo
Simply sizzle

Do you feel like a home cooked meal but don't like shopping, peeling, chopping, cooking, or cleaning up?

We deliver ready to roast free range chicken and fresh vegetables to your door.

To order: SMS your name to 074 318 6149 and we'll call you back.

Only the best ingredients used
Free range chickens. Fresh herbs and vegetables. Virgin olive oil.

No bad carbs!

Ready to roast Free range chicken and fresh veggies
For 2 R99
For 4 R139
Updates

Wording of flyer updated.

Target Market(s)

Local Cape Townians that hate grocery shopping and need help saving time preparing meals.

Industry/Entity Type

Delivery Service

Requirements
Must have
• To find out more: SMS your name to 074 318 6149

```html
<!DOCTYPE html>
<html lang="en">
<head>
<meta charset="utf-8">
<title>Pemblo – Simply sizzle</title>
<link rel="stylesheet" href="https://fonts.googleapis.com/css2?family=Arimo:wght@400;700&family=Roboto+Slab:wght@700&display=swap">
<style>
  :root {
    --green-light: #9fd142;
    --green-mid: #5aa829;
    --green-dark: #2a6e16;
    --red: #d42027;
    --red-dark: #9e1116;
    --white: #ffffff;
    --ink: #1b1b1b;
    --roast-gold: #d9a45a;
    --roast-brown: #8a5626;
  }
  * { margin: 0; padding: 0; box-sizing: border-box; }
  html, body { width: 927px; height: 1200px; overflow: hidden; background: var(--white); }
  .flyer {
    position: relative;
    width: 927px;
    height: 1200px;
    overflow: hidden;
    font-family: "Arimo", Arial, sans-serif;
  }
  .flyer-art { position: absolute; inset: 0; width: 927px; height: 1200px; }

  .brand {
    position: absolute;
    top: 14px;
    left: 0;
    width: 100%;
    text-align: center;
    color: var(--red);
    font-weight: 700;
  }
  .brand-name { display: block; font-size: 110px; line-height: 1; letter-spacing: 1px; }
  .brand-tagline { display: block; font-size: 40px; line-height: 1; margin-top: 2px; }

  .headline {
    position: absolute;
    top: 202px;
    left: 0;
    width: 100%;
    text-align: center;
    color: var(--white);
    font-weight: 700;
    font-size: 31px;
    line-height: 38px;
  }

  .intro {
    position: absolute;
    top: 318px;
    left: 50px;
    width: 420px;
    color: var(--ink);
    font-size: 20px;
    line-height: 25px;
  }
  .intro p + p { margin-top: 24px; }

  .price-badge {
    position: absolute;
    left: 48px;
    top: 586px;
    width: 286px;
    height: 286px;
    padding-top: 26px;
    text-align: center;
    color: var(--white);
  }
  .price-badge-lead { font-size: 20px; line-height: 23px; }
  .price-list { margin-top: 6px; font-weight: 700; line-height: 50px; }
  .price-row { display: block; font-size: 46px; white-space: nowrap; }
  .price-for { font-size: 30px; }
  .price-currency { font-size: 22px; vertical-align: 16px; margin-left: 12px; }

  .website {
    position: absolute;
    bottom: 30px;
    left: 0;
    width: 100%;
    text-align: center;
    color: var(--white);
    font-family: "Roboto Slab", Georgia, serif;
    font-weight: 700;
    font-size: 30px;
    letter-spacing: 1px;
  }
</style>
</head>
<body>
<main class="flyer">
  <svg class="flyer-art" viewBox="0 0 680 880" preserveAspectRatio="none">
    <defs>
      <radialGradient id="green-field" cx="50%" cy="35%" r="75%">
        <stop offset="0" stop-color="var(--green-light)"/>
        <stop offset="0.55" stop-color="var(--green-mid)"/>
        <stop offset="1" stop-color="var(--green-dark)"/>
      </radialGradient>
      <radialGradient id="roast-tones" cx="55%" cy="45%" r="60%">
        <stop offset="0" stop-color="#f1c98a"/>
        <stop offset="0.5" stop-color="var(--roast-gold)"/>
        <stop offset="0.85" stop-color="var(--roast-brown)"/>
        <stop offset="1" stop-color="#b8322a"/>
      </radialGradient>
      <radialGradient id="badge-red" cx="45%" cy="40%" r="65%">
        <stop offset="0" stop-color="#ec3b3f"/>
        <stop offset="1" stop-color="var(--red-dark)"/>
      </radialGradient>
      <linearGradient id="footer-red" x1="0" y1="0" x2="0" y2="1">
        <stop offset="0" stop-color="var(--red)"/>
        <stop offset="1" stop-color="var(--red-dark)"/>
      </linearGradient>
      <path id="order-curve" d="M0,640 Q340,895 680,650"/>
    </defs>

    <rect class="background" width="680" height="880" fill="url(#green-field)"/>

    <g class="food-photo" role="img" aria-label="Photo of a golden roast free range chicken on a white dish with red peppers, red onions, potatoes, lemon and fresh herbs">
      <circle cx="505" cy="482" r="245" fill="url(#roast-tones)" stroke="#f4f1e8" stroke-width="4"/>
    </g>

    <circle class="badge-disc" cx="140" cy="535" r="105" fill="url(#badge-red)" stroke="#f3d0cf" stroke-width="2"/>

    <path class="footer-band" d="M0,650 Q340,940 680,680 L680,880 L0,880 Z" fill="url(#footer-red)"/>
    <path class="order-band" d="M0,598 Q340,850 680,600 L680,690 Q340,920 0,660 Z" fill="var(--white)"/>

    <text class="order-line" font-family="Arimo, Arial, sans-serif" font-weight="700" font-size="21" fill="var(--ink)">
      <textPath href="#order-curve" startOffset="50%" text-anchor="middle">To order: SMS your name to 074 318 6149 and we’ll call you back</textPath>
    </text>
  </svg>

  <header class="brand">
    <span class="brand-name">Pemblo</span>
    <span class="brand-tagline">Simply sizzle</span>
  </header>

  <h1 class="headline">Do you feel like a home cooked meal but don’t like<br>shopping, peeling, chopping, cooking, or cleaning up?</h1>

  <section class="intro">
    <p>We deliver ready to roast free<br>range chicken and fresh vegetables<br>to your door.</p>
    <p>Only the best ingredients used.<br>Free range chickens.<br>Fresh herbs and vegetables.<br>Virgin olive oil.</p>
    <p>No bad carbs!</p>
  </section>

  <aside class="price-badge">
    <p class="price-badge-lead">Ready<br>to roast Free<br>range chicken and<br>fresh veggies</p>
    <p class="price-list">
      <span class="price-row"><span class="price-for">for</span>2<span class="price-currency">R</span>99</span>
      <span class="price-row"><span class="price-for">for</span>4<span class="price-currency">R</span>139</span>
    </p>
  </aside>

  <footer class="website">www.pemblo.co.za</footer>
</main>
</body>
</html>
```